eco friendly packagin cat litter

I would like to purchase a customized version of a design you have previously submitted - https://www.plintora.com/design/58170943<br/><br/>we look for a graphic for a pack of litter pellets for cats (and small rodents), the indications of the icons are fine as the example mock-up, we just have to add the possibility of disposing in the toilet!All entries must be in Italian, the product will be called FURO NUGGET - the subtitle will be "ecological litter for cats and small rodents" LETTIERA ECOLOGICA PER GATTI E PICCOLI RODITORII would like the main image to be of the cat, but I would like the icons to show also rabbits and hamsters.how can I intervene on the texts to give you a hand?I'd like to have a transparent window (not at the base) where you can see the wood pellet.you can see the dimensions from the pen drawing.the Silvatek Nordia logo, is the name of our company. I would like it to be present in the pack but not too big.I like the atmosphere of your example pack but I also like the one in the attached photo "REED KITTY SAND"
Target Market(s)
supermarket and pet food stores
Requirements
Must have
- -a cat
- -eco friendly - aspect
- -a transparent window to show the wood pellets
- -an icon list for product qualities
- -high absorbency (Alto potere assorbente)
- eliminates odors (elimina gli odori)
- 100% natural / ecological (100% naturale)
- cheap- (economico)
- -long time (lunga durata)
- does not stick to the legs (non si attacca alle zampe)
- - a "FURO NUGGET" international looking logo
- Must be in Italian language

```html
<!DOCTYPE html>
<html lang="it">
<head>
<meta charset="utf-8">
<title>FURO NUGGET – Lettiera ecologica</title>
<link href="https://fonts.googleapis.com/css2?family=Ubuntu:wght@500;700&display=swap" rel="stylesheet">
<style>
  :root{
    --bg:#ffffff;
    --bag-brown:#5b2f1f;
    --bag-brown-dark:#4a2417;
    --cream:#efe6d2;
    --leaf:#5a7a26;
    --leaf-light:#86a845;
    --ink:#4a2418;
    --icon-ring:#e8dcc2;
    --white:#ffffff;
  }
  *{box-sizing:border-box;margin:0;padding:0}
  html,body{width:1200px;height:901px;overflow:hidden;background:var(--bg)}
  body{position:relative;font-family:"Ubuntu",sans-serif}

  .pack{position:absolute;top:52px;width:515px;height:752px;
    clip-path:polygon(0 0,100% 0,100% 18%,92% 100%,9% 100%,0 18%)}
  .pack--en{left:65px}
  .pack--it{left:621px}

  .pack__top{position:absolute;left:0;top:0;width:515px;height:138px;
    background:linear-gradient(180deg,var(--bag-brown) 0 55%,#8c6f63 75%,var(--bag-brown) 100%)}
  .pack__handle{position:absolute;left:168px;top:27px;width:179px;height:76px;
    border-radius:38px;background:var(--bg);box-shadow:inset 0 -4px 8px rgba(0,0,0,.15)}

  .pack__body{position:absolute;left:0;top:138px;width:515px;height:535px;
    background:linear-gradient(90deg,var(--leaf-light) 0 6%,var(--cream) 6% 100%)}
  .pack__photo{position:absolute;left:272px;top:0;width:240px;height:535px;
    background:radial-gradient(ellipse at 55% 45%,#f4f1ea 0 22%,#e7a866 40%,#d58a45 65%,#b9c48e 100%)}
  .pack__pets{position:absolute;left:323px;top:443px;width:125px;height:128px;border-radius:40px 40px 10px 10px;
    background:radial-gradient(circle at 50% 40%,#f1ece8,#c9b8ad 70%,rgba(201,184,173,0) 100%)}

  .pack__panel{position:absolute;left:40px;top:0;width:240px;height:535px;text-align:center;color:var(--ink)}
  .brand{margin-top:42px;color:var(--leaf);font-weight:700;line-height:.9}
  .brand__name{display:block;font-size:80px;letter-spacing:1px}
  .brand__line{display:block;font-size:34px;letter-spacing:4px;margin-top:10px}
  .subtitle{margin-top:34px;font-size:18px;font-weight:700;line-height:27px;text-transform:uppercase}
  .rule{position:absolute;left:19px;top:329px;width:210px;height:2px;background:var(--ink)}
  .badge{position:absolute;left:50px;top:344px;width:135px;height:58px;border-radius:28px 8px 28px 8px;
    background:var(--leaf);color:var(--white);display:flex;flex-direction:column;align-items:center;justify-content:center}
  .badge__big{font-size:18px;font-weight:700;line-height:18px}
  .badge__small{font-size:7px;font-weight:700;margin-top:3px}
  .window{position:absolute;left:9px;top:419px;width:231px;height:92px;border-radius:10px;
    background:repeating-linear-gradient(35deg,#d9c49c 0 9px,#b89a6a 9px 12px,#e8d9b8 12px 20px);
    box-shadow:inset 0 0 0 2px rgba(255,255,255,.5)}
  .net{position:absolute;left:0;top:515px;width:240px;font-size:15px;font-weight:500;letter-spacing:.5px}

  .pack__base{position:absolute;left:0;top:673px;width:515px;height:79px;background:var(--bag-brown-dark)}
  .icons{position:absolute;left:58px;top:15px;display:flex;gap:9px;list-style:none}
  .icons li{width:34px;height:34px;border-radius:50%;border:2px solid var(--icon-ring);background:#6b3b29;
    color:var(--icon-ring);font-size:4px;font-weight:700;line-height:5px;text-align:center;overflow:hidden;
    display:flex;align-items:flex-end;justify-content:center;padding:0 3px 5px}
  .maker{position:absolute;left:355px;top:47px;color:var(--white);font-size:10px;font-weight:700;display:flex;align-items:center;gap:3px}
  .maker__dot{width:6px;height:6px;border-radius:50%;background:var(--leaf-light)}
</style>
</head>
<body>

<section class="pack pack--en" aria-label="Confezione in inglese">
  <div class="pack__top"><div class="pack__handle"></div></div>
  <div class="pack__body">
    <div class="pack__photo" role="img" aria-label="Photo of a ginger kitten sitting"></div>
    <div class="pack__pets" role="img" aria-label="Photo of a rabbit, guinea pig and hamster"></div>
    <div class="pack__panel">
      <h1 class="brand"><span class="brand__name">FURO</span><span class="brand__line">NUGGET</span></h1>
      <p class="subtitle">Ecological litter<br>for cats and<br>small rodents</p>
      <div class="rule"></div>
      <div class="badge"><span class="badge__big">100%<br>NATURAL</span><span class="badge__small">NO PRESERVATIVES</span></div>
      <div class="window" role="img" aria-label="Transparent window showing wood pellets"></div>
      <p class="net">NET WT ℮7L</p>
    </div>
  </div>
  <div class="pack__base">
    <ul class="icons">
      <li>HYPER ABSORBENT</li><li>HIGH ODOUR CONTROL</li><li>ULTRA CLUMPING</li>
      <li>LONG LASTING</li><li>FLUSH ABLE</li><li>NON STICK</li>
    </ul>
    <div class="maker"><span class="maker__dot"></span>Silvatek Nordia</div>
  </div>
</section>

<section class="pack pack--it" aria-label="Confezione in italiano">
  <div class="pack__top"><div class="pack__handle"></div></div>
  <div class="pack__body">
    <div class="pack__photo" role="img" aria-label="Foto di un gattino rosso seduto"></div>
    <div class="pack__pets" role="img" aria-label="Foto di coniglio, porcellino d'India e criceto"></div>
    <div class="pack__panel">
      <h2 class="brand"><span class="brand__name">FURO</span><span class="brand__line">NUGGET</span></h2>
      <p class="subtitle">Lettiera ecologica<br>per gatti e piccoli<br>roditori</p>
      <div class="rule"></div>
      <div class="badge"><span class="badge__big">100%<br>NATURAL</span><span class="badge__small">SENZA ADDITIVI</span></div>
      <div class="window" role="img" aria-label="Finestra trasparente con pellet di legno"></div>
      <p class="net">PESO NETTO ℮7L</p>
    </div>
  </div>
  <div class="pack__base">
    <ul class="icons">
      <li>SUPER ASSORBENTE</li><li>ELIMINA ODORI</li><li>ULTRA COMPATTA</li>
      <li>LUNGA DURATA</li><li>BIO DEGRADA BILE</li><li>NON SI ATTACCA</li>
    </ul>
    <div class="maker"><span class="maker__dot"></span>Silvatek Nordia</div>
  </div>
</section>

</body>
</html>
```